Health and Wellbeing online Shop

I have attached a specification, however in summary this is a new business startup selling vitamins and supplements.

We need a web design for new wellbeing website, selling high end vitamins, supplements and nootropics. Therefore I need a simple eCommerce solution .

I need the website to look very different to other websites on the market. The more creative the better. It should look fresh elegant and simple. The criteria for products being on my site is that they have great reviews and they have been scientifically tested.

You will need the option of being able to log into an account, either through pagebook, snoople, chirpnet, Pixogram or create an account with email. For accounts, users will need the facility to reset passwords, see previous orders, track current order, and maintain favourites.

It should be PC, mobile and tablet friendly.

Look and Feel

It should be an elegant, modern, professional, trendy, unisex website. It should look clean and calm. Am happy to try interesting and slightly unusual designs. I would also like to have chat functionality, either powered by volKAtalk or by Bax 61.

Websites I like are
https://www.corvan-radiance.co.uk/
https://www.plainnutrients.co.uk/
http://www.lumadermis.com/

PLEASE DO USE YOUR KNOWELDGE OF WHAT WORKS FOR WEB DESIGN. YOU’RE THE EXPERT AND NEED YOUR EXPERTISE. CARTE BLANCHE TO DESIGN AS YOU SEE FIT. Please be creative, I need my site to stand out from the crowd.

Target Market(s)
Middle aged women are our most common client, however, younger patients, both male and female, will often visit the site. In summary, I would like the site to appeal to all age brackets.

Industry/Entity Type
Business

Coding
Coded - Design and coding required

Number of Pages Required
5 pages
Updates

I would like more designs. I was expecting 75+ Designs to choose from as per the package I paid for.

Target Market(s)

Industry/Entity Type

Health And Wellness

Coding

Number of Pages Required

5+ page

Requirements
Must have
• Creative design

```html
<!DOCTYPE html>
<html lang="en">
<head>
<meta charset="utf-8">
<title>Nexa Skin Clinic — Shop</title>
<link rel="stylesheet" href="https://fonts.googleapis.com/css2?family=Libre+Baskerville:wght@400;700&family=Questrial&family=Montserrat:wght@500;600;700&display=swap">
<style>
:root{
  --yellow:#f2c72c;
  --gold:#e6b622;
  --tan:#b58e3f;
  --cream:#fdf6dc;
  --teal:#7dd8cb;
  --ink:#1d1d1d;
  --muted:#555;
  --white:#fff;
}
*{margin:0;padding:0;box-sizing:border-box}
html,body{width:1200px;height:3097px;overflow:hidden}
body{position:relative;background:var(--white);font-family:"Questrial",sans-serif;color:var(--ink)}
.abs{position:absolute}
.serif{font-family:"Libre Baskerville",serif}
.sans-bold{font-family:"Montserrat",sans-serif;font-weight:700}

/* top bar */
.topbar{left:0;top:0;width:1200px;height:48px;background:var(--yellow)}
.topbar span{position:absolute;top:17px;font-family:"Montserrat",sans-serif;font-weight:700;font-size:12.5px;color:#3a2e10;letter-spacing:.3px}

/* header */
.phone-dot{left:113px;top:80px;width:48px;height:48px;border-radius:50%;background:var(--yellow)}
.call-label{left:174px;top:84px;font-size:14px;font-family:"Montserrat",sans-serif;font-weight:600}
.call-number{left:167px;top:104px;font-size:26px;font-family:"Libre Baskerville",serif}
.brand-mark{left:561px;top:64px;width:80px;height:80px;border-radius:50%;border:2px solid var(--ink);display:flex;align-items:center;justify-content:center;font-family:"Libre Baskerville",serif;font-size:20px}
.search{left:707px;top:83px;width:301px;height:46px;border:2px solid #333;border-radius:23px}
.search span{position:absolute;left:78px;top:13px;font-size:13.5px;color:#555}
.cart{left:1046px;top:82px;width:47px;height:47px;border-radius:50%;background:var(--yellow)}
.cart-badge{left:1078px;top:78px;width:21px;height:21px;border-radius:50%;background:#e1121b;color:#fff;font-size:12px;text-align:center;line-height:21px;font-family:"Montserrat",sans-serif;font-weight:700}
.header-rule{left:60px;top:159px;width:1080px;height:1px;background:#bbb}

/* nav */
.nav a{position:absolute;top:182px;font-family:"Montserrat",sans-serif;font-weight:700;font-size:13.5px;color:var(--ink);text-decoration:none}
.nav a.active{color:var(--yellow)}
.nav-underline{left:165px;top:221px;width:67px;height:4px;background:var(--yellow)}
.nav-social span{position:absolute;top:180px;font-family:"Montserrat",sans-serif;font-weight:700;font-size:15px}

/* hero */
.hero{left:0;top:225px;width:1200px;height:595px;background:linear-gradient(90deg,#6fd3c6 0%,#82dccf 45%,#7ad6c9 100%);border-bottom:4px solid var(--yellow)}
.hero-title{left:640px;top:335px;font-family:"Libre Baskerville",serif;font-size:54px;line-height:62px;color:var(--white);letter-spacing:1px}
.hero-title em{font-style:normal;color:var(--yellow);font-size:48px}
.hero-copy{left:640px;top:470px;width:475px;font-size:16.5px;line-height:30px;color:var(--white)}
.btn{position:absolute;display:flex;align-items:center;justify-content:center;border-radius:30px;font-family:"Libre Baskerville",serif;font-size:16px;color:var(--ink);background:var(--yellow)}

/* offers */
.offer{height:255px;border-radius:8px;box-shadow:0 6px 16px rgba(0,0,0,.12);overflow:hidden}
.offer-1{left:112px;top:908px;width:477px;background:linear-gradient(135deg,#f8c4a1,#fcdcc4)}
.offer-2{left:610px;top:908px;width:478px;background:linear-gradient(180deg,#f0efec,#e3e1dc)}
.offer h3{position:absolute;font-family:"Libre Baskerville",serif;font-weight:400;font-size:27px;color:var(--ink)}
.offer p{position:absolute;font-family:"Libre Baskerville",serif;font-size:27px;color:var(--gold)}

/* shop */
.shop{left:0;top:1248px;width:1200px;height:1097px;background:var(--cream)}
.filter{left:112px;width:222px;height:52px;background:var(--yellow);border-radius:3px}
.filter span{position:absolute;left:40px;top:17px;font-family:"Montserrat",sans-serif;font-weight:600;font-size:16px}
.filter i{position:absolute;right:22px;top:23px;border:6px solid transparent;border-top:6px solid var(--ink)}
.panel{left:112px;width:222px;border-radius:3px}
.panel h4{position:absolute;font-family:"Libre Baskerville",serif;font-weight:400;font-size:16px}
.social-dot{position:absolute;top:1627px;width:30px;height:30px;border-radius:50%;background:var(--yellow);font-family:"Montserrat",sans-serif;font-weight:700;font-size:13px;text-align:center;line-height:30px;color:var(--ink)}
.stars{position:absolute;color:var(--yellow);font-size:17px;letter-spacing:3px}
.stars b{font-weight:400;color:var(--white)}
.score-num{position:absolute;left:298px;color:var(--white);font-size:15px}
.sortby{left:365px;top:1334px;width:275px;height:48px;background:var(--white);box-shadow:0 2px 6px rgba(0,0,0,.12)}
.sortby span{position:absolute;left:13px;top:15px;font-family:"Montserrat",sans-serif;font-weight:500;font-size:13px}
.product-img{position:absolute;width:234px;height:253px;background:radial-gradient(ellipse 60px 100px at 50% 48%,#dcdcdc 0%,#f1f1f1 60%,#ffffff 100%)}
.product-name{position:absolute;width:234px;text-align:center;font-family:"Libre Baskerville",serif;font-size:16px}
.product-price{position:absolute;width:234px;text-align:center;font-size:18px;color:var(--gold)}
.product-stars{position:absolute;width:234px;text-align:center;color:var(--yellow);font-size:15px;letter-spacing:4px}
.btn-outline{position:absolute;width:157px;height:40px;border:2px solid var(--yellow);border-radius:20px;text-align:center;line-height:36px;font-family:"Libre Baskerville",serif;font-size:16px;color:var(--yellow)}
.btn-outline.filled{background:var(--yellow);color:var(--ink)}

/* testimonials */
.testimonials{left:0;top:2345px;width:1200px;height:406px;background:var(--yellow)}
.testimonials h2{position:absolute;left:0;top:83px;width:1200px;text-align:center;font-family:"Libre Baskerville",serif;font-weight:400;font-size:34px;color:#4a3610}
.testimonials .rule{position:absolute;left:557px;top:138px;width:69px;height:2px;background:#4a3610}
.testimonials p{position:absolute;left:155px;top:166px;width:890px;text-align:center;font-size:17.5px;line-height:30px;color:#4a3610}
.testimonials .author{position:absolute;left:0;top:295px;width:1200px;text-align:center;font-family:"Libre Baskerville",serif;font-weight:700;font-size:18px;color:#4a3610}

/* footer */
.footer-mark{left:118px;top:2821px;width:102px;height:102px;border-radius:50%;border:2px solid var(--ink);display:flex;align-items:center;justify-content:center;font-family:"Libre Baskerville",serif;font-size:24px}
.pay{position:absolute;top:2947px;width:34px;height:22px;border-radius:3px;background:#2b2b2b;color:#fff;font-size:7.5px;text-align:center;line-height:22px}
.foot-col h5{position:absolute;font-family:"Montserrat",sans-serif;font-weight:600;font-size:13px;letter-spacing:.2px}
.foot-col a{position:absolute;font-size:12.5px;color:var(--muted);text-decoration:none}
.foot-input{left:684px;top:2910px;width:266px;height:44px;border:1px solid #ccc;background:#f3f3f3}
.foot-input span{position:absolute;left:19px;top:15px;font-size:12.5px;color:#444}
.foot-btn{left:958px;top:2910px;width:128px;height:44px;background:var(--yellow);text-align:center;line-height:44px;font-family:"Montserrat",sans-serif;font-weight:700;font-size:14px}
.foot-social{position:absolute;top:2972px;width:33px;height:33px;border-radius:50%;background:var(--ink);color:#fff;font-family:"Montserrat",sans-serif;font-weight:700;font-size:12px;text-align:center;line-height:33px}
.foot-rule{left:94px;top:3031px;width:976px;height:1px;background:#999}
.copyright{left:0;top:3054px;width:1200px;text-align:center;font-size:12px;color:#444}
</style>
</head>
<body>

<!-- top bar -->
<div class="abs topbar">
  <span style="left:114px">CHECKOUT &nbsp;| &nbsp;CART &nbsp;| &nbsp;SHOP</span>
  <span style="left:603px">TRACK CURRENT ORDER</span>
  <span style="left:836px">LOGIN</span>
  <span style="left:939px">CREATE AN ACCOUNT</span>
</div>

<!-- header -->
<div class="abs phone-dot">
  <svg width="48" height="48" viewBox="0 0 48 48"><path d="M19 17c1 4 4 9 10 12l2-2c.6-.6 1.4-.6 2 0l2 2c.6.6.6 1.4 0 2-3 3-8 1-12-3s-6-9-3-12c.6-.6 1.4-.6 2 0l2 2c.6.6.6 1.4 0 2z" fill="#1d1d1d"/></svg>
</div>
<div class="abs call-label">Call Us Today</div>
<div class="abs call-number">01632 960418</div>
<div class="abs brand-mark">Nexa</div>
<div class="abs search">
  <svg class="abs" style="left:20px;top:13px" width="18" height="18" viewBox="0 0 18 18"><circle cx="7.5" cy="7.5" r="5.5" fill="none" stroke="#e6b622" stroke-width="2.4"/><path d="M11.5 11.5l5 5" stroke="#e6b622" stroke-width="2.6"/></svg>
  <span>Search The Here</span>
</div>
<div class="abs cart">
  <svg width="47" height="47" viewBox="0 0 47 47"><path d="M16 20h15l-1 11H17z" fill="#1d1d1d"/><path d="M19 20v-2a4.5 4.5 0 0 1 9 0v2" fill="none" stroke="#1d1d1d" stroke-width="2"/></svg>
</div>
<div class="abs cart-badge">2</div>
<div class="abs header-rule"></div>

<!-- nav -->
<nav class="nav">
  <a class="active" style="left:176px">HOME</a>
  <a style="left:258px">ABOUT US</a>
  <a style="left:364px">VITAMINS</a>
  <a style="left:477px">NOOTROPICS</a>
  <a style="left:607px">REVIEWS</a>
  <a style="left:705px">CONTACT</a>
</nav>
<div class="abs nav-underline"></div>
<div class="nav-social">
  <span style="left:891px">P</span>
  <span style="left:935px">X</span>
  <span style="left:980px">C</span>
  <span style="left:1023px">S</span>
</div>

<!-- hero -->
<section class="abs hero" role="img" aria-label="Photo of a smiling woman holding orange slices in front of a teal background with leaves and capsules"></section>
<h1 class="abs hero-title">WELCOME TO<br><em>NEXA SKIN CLINIC</em></h1>
<p class="abs hero-copy">Welcome to Nexa Skin Clinic, leading supplier of skincare and beauty products. From must-have anti ageing products, to pigmentation correction.</p>
<div class="btn" style="left:640px;top:581px;width:192px;height:50px">SHOP NOW</div>

<!-- offers -->
<div class="abs offer offer-1">
  <div class="abs" role="img" aria-label="Supplement bottle with golden capsules and green leaves on a peach background" style="left:230px;top:0;width:247px;height:255px;background:radial-gradient(circle at 60% 45%,#fff8ef 0%,#f7d1b0 55%,#f6c3a0 100%)"></div>
  <h3 style="left:36px;top:55px">SPECIAL OFFER</h3>
  <p style="left:36px;top:98px">30% OFF</p>
  <div class="btn" style="left:37px;top:157px;width:192px;height:50px">SHOP NOW</div>
</div>
<div class="abs offer offer-2">
  <div class="abs" role="img" aria-label="Wooden spoons holding assorted pills and capsules on white wood" style="left:60px;top:95px;width:418px;height:160px;background:linear-gradient(180deg,rgba(225,223,218,0) 0%,#b08a62 55%,#7a4a2a 100%)"></div>
  <h3 style="left:23px;top:33px">SPECIAL OFFER</h3>
  <p style="left:31px;top:75px">30% OFF</p>
  <div class="btn" style="left:278px;top:28px;width:192px;height:51px">SHOP NOW</div>
</div>

<!-- shop -->
<section class="abs shop"></section>

<div class="abs filter" style="top:1334px"><span>CATEGORY</span><i></i></div>
<div class="abs filter" style="top:1392px"><span>INTEREST</span><i></i></div>
<div class="abs filter" style="top:1449px"><span>DELIVERY</span><i></i></div>
<div class="abs filter" style="top:1506px"><span>NEW</span><i></i></div>

<div class="abs panel" style="top:1575px;height:120px;background:var(--tan)">
  <h4 style="left:20px;top:16px;color:#fff">Stay In Touch</h4>
</div>
<div class="social-dot" style="left:127px">P</div>
<div class="social-dot" style="left:168px">X</div>
<div class="social-dot" style="left:209px;background:#fff">C</div>
<div class="social-dot" style="left:249px">N</div>
<div class="social-dot" style="left:290px">S</div>

<div class="abs panel" style="top:1710px;height:231px;background:var(--yellow)">
  <h4 style="left:20px;top:16px">NEWSLETTER</h4>
  <div class="abs" style="left:13px;top:47px;width:200px;font-size:12.5px;line-height:30px">Sign up to our newsletter for the latest news and special offers.</div>
  <div class="abs" style="left:13px;top:106px;width:190px;height:41px;background:#fff;border-radius:4px;font-size:12.5px;padding:13px 15px">Type your email</div>
  <div class="abs" style="left:15px;top:168px;width:153px;height:36px;background:var(--ink);border-radius:18px;color:var(--yellow);text-align:center;line-height:36px;font-family:'Libre Baskerville',serif;font-size:15px">SHOP NOW</div>
</div>

<div class="abs panel" style="top:1958px;height:250px;background:var(--tan)">
  <h4 style="left:21px;top:30px;color:var(--yellow)">REVIEW SCORE</h4>
</div>
<div class="stars" style="left:133px;top:2031px">★★★★★</div><div class="score-num" style="top:2034px">5</div>
<div class="stars" style="left:133px;top:2066px">★★★★<b>★</b></div><div class="score-num" style="top:2069px">4</div>
<div class="stars" style="left:133px;top:2100px">★★★<b>★★</b></div><div class="score-num" style="top:2103px">3</div>
<div class="stars" style="left:133px;top:2134px">★★<b>★★★</b></div><div class="score-num" style="top:2137px">2</div>
<div class="stars" style="left:133px;top:2168px">★<b>★★★★</b></div><div class="score-num" style="top:2171px">1</div>

<div class="abs sortby"><span>Sort by</span>
  <svg class="abs" style="left:249px;top:21px" width="10" height="6" viewBox="0 0 10 6"><path d="M0 0h10L5 6z" fill="#1d1d1d"/></svg>
</div>
<svg class="abs" style="left:987px;top:1338px" width="105" height="24" viewBox="0 0 105 24">
  <g fill="#555"><rect x="0" y="6" width="16" height="2"/><rect x="0" y="10" width="12" height="2"/><rect x="0" y="14" width="16" height="2"/><rect x="0" y="18" width="12" height="2"/></g>
  <g fill="#555"><rect x="37" y="0" width="10" height="10"/><rect x="49" y="0" width="10" height="10"/><rect x="37" y="12" width="10" height="10"/><rect x="49" y="12" width="10" height="10"/></g>
  <rect x="77" y="-1" width="27" height="25" fill="#fff" stroke="#ccc"/>
  <g fill="#1d1d1d"><rect x="80" y="2" width="6" height="6"/><rect x="88" y="2" width="6" height="6"/><rect x="96" y="2" width="6" height="6"/><rect x="80" y="10" width="6" height="6"/><rect x="88" y="10" width="6" height="6"/><rect x="96" y="10" width="6" height="6"/><rect x="80" y="18" width="6" height="4"/><rect x="88" y="18" width="6" height="4"/><rect x="96" y="18" width="6" height="4"/></g>
</svg>

<!-- product row 1 -->
<div class="product-img" style="left:365px;top:1416px" role="img" aria-label="White supplement bottle"></div>
<div class="product-img" style="left:609px;top:1416px" role="img" aria-label="White supplement bottle"></div>
<div class="product-img" style="left:853px;top:1416px" role="img" aria-label="White supplement bottle"></div>
<div class="product-name" style="left:365px;top:1688px">BODY CARE</div>
<div class="product-name" style="left:609px;top:1688px">BUZZ PRODUCT</div>
<div class="product-name" style="left:853px;top:1688px">HAIR PRODUCT</div>
<div class="product-price" style="left:365px;top:1713px">$35 per Bottle</div>
<div class="product-price" style="left:609px;top:1713px">$21.99 per Bottle</div>
<div class="product-price" style="left:853px;top:1713px">$21.99 per Bottle</div>
<div class="product-stars" style="left:365px;top:1739px">★★★★★</div>
<div class="product-stars" style="left:609px;top:1739px">★★★★★</div>
<div class="product-stars" style="left:853px;top:1739px">★★★★★</div>
<div class="btn-outline" style="left:404px;top:1776px">SHOP NOW</div>
<div class="btn-outline filled" style="left:648px;top:1776px">SHOP NOW</div>
<div class="btn-outline" style="left:892px;top:1776px">SHOP NOW</div>

<!-- product row 2 -->
<div class="product-img" style="left:365px;top:1856px" role="img" aria-label="White supplement bottle"></div>
<div class="product-img" style="left:609px;top:1856px" role="img" aria-label="White supplement bottle"></div>
<div class="product-img" style="left:853px;top:1856px" role="img" aria-label="White supplement bottle"></div>
<div class="product-name" style="left:365px;top:2124px">SKIN PRODUCT</div>
<div class="product-name" style="left:609px;top:2127px">FRAGRANCE</div>
<div class="product-name" style="left:853px;top:2127px">BUZZ</div>
<div class="product-price" style="left:365px;top:2152px">$20 per Bottle</div>
<div class="product-price" style="left:609px;top:2152px">$41.99 per Bottle</div>
<div class="product-price" style="left:853px;top:2152px">$12 per Bottle</div>
<div class="product-stars" style="left:365px;top:2178px">★★★★★</div>
<div class="product-stars" style="left:609px;top:2178px">★★★★★</div>
<div class="product-stars" style="left:853px;top:2178px">★★★★★</div>
<div class="btn-outline" style="left:404px;top:2216px">SHOP NOW</div>
<div class="btn-outline" style="left:648px;top:2216px">SHOP NOW</div>
<div class="btn-outline" style="left:892px;top:2216px">SHOP NOW</div>

<!-- testimonials -->
<section class="abs testimonials">
  <h2>Our Client Testimonials</h2>
  <div class="rule"></div>
  <p>Lorem ipsum dolor sit amet, consectetur adipiscing elit, sed do eiusmod tempor incididunt ut labore et dolore magna aliqua. Ut enim ad minim veniam, quis nostrud exercitation ullamco laboris nisi ut aliquip ex ea commodo consequat. Duis aute irure dolor in reprehenderit in voluptate velit esse cillum dolore eu fugiat nulla pariatur. Excepteur sint occaecat cupidatat non proident, sunt in culpa qui officia deserunt mollit anim id est laborum</p>
  <div class="author">Mira Holt</div>
  <svg class="abs" style="left:66px;top:193px" width="16" height="48" viewBox="0 0 16 48"><path d="M14 1L2 24l12 23" fill="none" stroke="#3a2a0c" stroke-width="2"/></svg>
  <svg class="abs" style="left:1117px;top:193px" width="16" height="48" viewBox="0 0 16 48"><path d="M2 1l12 23L2 47" fill="none" stroke="#3a2a0c" stroke-width="2"/></svg>
</section>

<!-- footer -->
<div class="abs footer-mark">Nexa</div>
<div class="pay" style="left:70px;border-radius:11px">Orbis</div>
<div class="pay" style="left:113px;background:#fff;color:#222;border:1px solid #999">Vanta</div>
<div class="pay" style="left:156px;background:#1d1d1d">Kora</div>
<div class="pay" style="left:198px">Meridia</div>
<div class="pay" style="left:240px">Paylo</div>

<div class="foot-col">
  <h5 style="left:321px;top:2820px">COMPANY</h5>
  <a style="left:321px;top:2856px">Home</a>
  <a style="left:321px;top:2883px">About Us</a>
  <a style="left:321px;top:2909px">Vitamins</a>
  <a style="left:321px;top:2935px">Nootropics</a>
  <a style="left:321px;top:2962px">Contact</a>

  <h5 style="left:490px;top:2820px">INFORMATION</h5>
  <a style="left:490px;top:2856px">Terms &amp; Conditions</a>
  <a style="left:490px;top:2883px">Privacy Policy</a>
  <a style="left:490px;top:2909px">Disclaimer</a>
  <a style="left:490px;top:2935px">Site Map</a>
  <a style="left:490px;top:2965px">Shipping Policy</a>
  <a style="left:490px;top:2995px">FAQ</a>

  <h5 style="left:684px;top:2820px">SUBSCRIBE OUR NEWSLETTER</h5>
  <a style="left:684px;top:2856px;width:320px;line-height:18px">Subscribe to our mailing list to receives daily updates direct to your inbox!</a>
</div>
<div class="abs foot-input"><span>Email Address</span></div>
<div class="abs foot-btn">SUBSCRIBE</div>
<div class="foot-social" style="left:681px">P</div>
<div class="foot-social" style="left:727px">X</div>
<div class="foot-social" style="left:773px">C</div>
<div class="foot-social" style="left:818px">N</div>

<div class="abs foot-rule"></div>
<div class="abs copyright">© Copyrights 2021 Nexa Health &nbsp; | &nbsp; All Rights Reserved</div>

</body>
</html>
```